Clean, Throwback Album Art needed

I'm looking for album art for an Indie Rock EP titled "The Farther Meridian". The artist name is "Colin Vasquez"

I'm looking for a design that's wistful and nostalgic, but not depressing. I'm more interested in creative patterns and color combinations than anything else. I've uploaded two examples of album art I really like.

Please no stock images.

In addition to the album art, I will also need two variants of a back cover created in a complementary style- one with a track listing and one with marketing copy (e.g. Free download available at ___ ). These back covers do not have to be incredibly detailed, but can't just be text overlaid on top of of the front cover.

Details for back cover (track names, credits, etc.) will be provided to whoever submits the winning front cover design.

Requirements
Should not have
• No stock images. I need to know that I fully own the copyright to whatever work is produced.

```html
<!DOCTYPE html>
<html lang="en">
<head>
<meta charset="utf-8">
<title>Colin Vasquez — The Farther Meridian</title>
<link href="https://fonts.googleapis.com/css2?family=Caveat:wght@500&family=Josefin+Sans:wght@300&display=swap" rel="stylesheet">
<style>
  :root {
    --teal: #22c2ba;
    --teal-deep: #1a9fb0;
    --blue: #1f6fc8;
    --blue-deep: #1b3fc4;
    --navy: #121f7a;
    --white: #ffffff;
  }
  html, body {
    margin: 0;
    padding: 0;
    overflow: hidden;
    background: #0e1a4a;
  }
  .cover {
    position: relative;
    width: 1200px;
    height: 1200px;
    overflow: hidden;
  }
  .cover__artwork {
    position: absolute;
    inset: 0;
    background:
      radial-gradient(ellipse 55% 45% at 92% 8%, rgba(18, 31, 122, 0.85), transparent 70%),
      linear-gradient(135deg, transparent 35%, rgba(27, 63, 196, 0.7) 48%, rgba(27, 63, 196, 0.7) 54%, transparent 66%),
      radial-gradient(ellipse 60% 50% at 5% 55%, rgba(34, 194, 186, 0.9), transparent 75%),
      radial-gradient(ellipse 60% 45% at 85% 95%, rgba(26, 159, 176, 0.9), transparent 75%),
      linear-gradient(160deg, var(--teal) 0%, var(--blue) 45%, var(--blue-deep) 60%, var(--teal-deep) 100%);
  }
  .cover__frame {
    position: absolute;
    left: 36px;
    top: 36px;
    width: 1128px;
    height: 1128px;
    box-sizing: border-box;
    border: 2.5px solid var(--white);
  }
  .artist {
    position: absolute;
    left: 190px;
    top: 532px;
    width: 788px;
    height: 140px;
    display: flex;
    align-items: center;
    justify-content: center;
    border-left: 3px solid var(--white);
    border-right: 3px solid var(--white);
    box-sizing: border-box;
    margin: 0;
    font-family: "Caveat", cursive;
    font-weight: 500;
    font-size: 112px;
    line-height: 1;
    color: var(--white);
    text-transform: lowercase;
    letter-spacing: 0.02em;
    word-spacing: 0.18em;
  }
  .title-rule {
    position: absolute;
    left: 466px;
    top: 972px;
    width: 268px;
    height: 3px;
    background: var(--white);
  }
  .title {
    position: absolute;
    left: 0;
    top: 1006px;
    width: 1200px;
    margin: 0;
    text-align: center;
    font-family: "Josefin Sans", sans-serif;
    font-weight: 300;
    font-size: 28px;
    line-height: 1;
    color: var(--white);
    text-transform: uppercase;
    letter-spacing: 0.95em;
    text-indent: 0.95em;
  }
</style>
</head>
<body>
  <main class="cover">
    <div class="cover__artwork" role="img" aria-label="Abstract artwork of overlapping translucent teal and blue curved panels radiating toward the upper right"></div>
    <div class="cover__frame"></div>
    <h1 class="artist">Colin Vasquez</h1>
    <div class="title-rule"></div>
    <h2 class="title">The Farther Meridian</h2>
  </main>
</body>
</html>
```